60 Ways to de-stress Poster

I would like a poster ( A4 full colour) with a list of 60 ways to destress. I would like the design to be clean and stylish (not cartoonish)

My Target market is stressed out mums so I want the poster to feel inspirational and relaxing to look at.

I have added a sample of something I like - but open to other ideas

Finished art would be print ready pdf

Target Market(s)

Mums who are stressed out - mainly new mums. I want this to be a poster that someone would happily put up that looks more like artwork.

Requirements
Must have
• My logo elements and colours but happy to incorporate other colours that blend well into it.

Colours:
Bright green: Pantone 376
Bright green as CMYK: c: 45.2% m: 0% y: 100% k: 0%

Logo text large grey: 70% black
Logo text strapline: 75% black
Tree: 80% black

Fonts:
Logo 'Willowbrook Calm': Verdana
Logo 'Counselling & coaching services for mums': Gill Sans Light
Should not have
• No cartoonish images - I want it very clean and stylish

```html
<!DOCTYPE html>
<html lang="en">
<head>
<meta charset="utf-8">
<title>60 Ways to de-stress — Willowbrook Calm</title>
<link rel="stylesheet" href="https://fonts.googleapis.com/css2?family=Open+Sans:wght@300;400;700&display=swap">
<style>
  :root {
    --backdrop: #ebe8e4;
    --paper: #ffffff;
    --purple: #8b2a8c;
    --blue: #1aa3dd;
    --green: #8dc63f;
    --orange: #f26a22;
    --pink: #e0185d;
    --title-grey: #6b6b6b;
    --logo-grey: #4d4d4d;
    --strap-grey: #404040;
  }
  * { box-sizing: border-box; }
  html, body {
    margin: 0;
    width: 1200px;
    height: 1000px;
    overflow: hidden;
    background: var(--backdrop);
  }
  .poster {
    position: absolute;
    left: 0;
    top: 73px;
    width: 1200px;
    height: 854px;
    display: block;
    background: var(--paper);
  }
  .spiral-text {
    font-family: "Open Sans", Verdana, sans-serif;
    font-size: 16px;
    font-weight: 400;
  }
  .way--purple { fill: var(--purple); }
  .way--blue { fill: var(--blue); }
  .way--green { fill: var(--green); }
  .way--orange { fill: var(--orange); }
  .way--pink { fill: var(--pink); }
  .poster-title {
    font-family: "Open Sans", Verdana, sans-serif;
    font-weight: 700;
    font-size: 29px;
    fill: var(--title-grey);
  }
  .brand-name {
    font-family: "Open Sans", Verdana, sans-serif;
    font-weight: 400;
    font-size: 19px;
    fill: var(--logo-grey);
  }
  .brand-strapline {
    font-family: "Open Sans", sans-serif;
    font-weight: 300;
    font-size: 11.5px;
    fill: var(--strap-grey);
  }
  .brand-dot { fill: var(--green); }
</style>
</head>
<body>
<svg class="poster" viewBox="50 95 1110 790" xmlns="http://www.w3.org/2000/svg" role="img" aria-label="60 Ways to de-stress poster">
  <defs>
    <path id="spiral-path" fill="none" d="M615,885
      A389.375,389.375 0 0 1 231.25,490
      A378.125,378.125 0 0 1 615,117.5
      A366.875,366.875 0 0 1 976.25,490
      A355.625,355.625 0 0 1 615,840
      A344.375,344.375 0 0 1 276.25,490
      A333.125,333.125 0 0 1 615,162.5
      A321.875,321.875 0 0 1 931.25,490
      A310.625,310.625 0 0 1 615,795
      A299.375,299.375 0 0 1 321.25,490
      A288.125,288.125 0 0 1 615,207.5
      A276.875,276.875 0 0 1 886.25,490
      A265.625,265.625 0 0 1 615,750
      A254.375,254.375 0 0 1 366.25,490
      A243.125,243.125 0 0 1 615,252.5
      A231.875,231.875 0 0 1 841.25,490
      A220.625,220.625 0 0 1 615,705
      A209.375,209.375 0 0 1 411.25,490
      A198.125,198.125 0 0 1 615,297.5
      A186.875,186.875 0 0 1 796.25,490
      A175.625,175.625 0 0 1 615,660
      A164.375,164.375 0 0 1 456.25,490
      A153.125,153.125 0 0 1 615,342.5
      A141.875,141.875 0 0 1 751.25,490
      A130.625,130.625 0 0 1 615,615
      A119.375,119.375 0 0 1 501.25,490
      A108.125,108.125 0 0 1 615,387.5
      A96.875,96.875 0 0 1 706.25,490
      A85.625,85.625 0 0 1 615,570
      A74.375,74.375 0 0 1 546.25,490"/>
  </defs>

  <rect class="poster-sheet" x="50" y="95" width="1110" height="790" fill="var(--paper)"/>

  <text class="spiral-text">
    <textPath href="#spiral-path" startOffset="170">
      <tspan class="way--green">Put on some music and dance</tspan>
      <tspan class="way--orange">Make a gratitude list</tspan>
      <tspan class="way--purple">Eat something mindfully</tspan>
      <tspan class="way--green">Go to the park</tspan>
      <tspan class="way--blue">Light a scented candle</tspan>
      <tspan class="way--purple">Buy yourself flowers</tspan>
      <tspan class="way--orange">Listening to music</tspan>
      <tspan class="way--purple">Call or visit a friend</tspan>
      <tspan class="way--pink">Take a nap</tspan>
      <tspan class="way--blue">Take some deep breaths</tspan>
      <tspan class="way--green">Take a mini mental holiday</tspan>
      <tspan class="way--green">Watch the clouds go by</tspan>
      <tspan class="way--blue">Have a bath</tspan>
      <tspan class="way--pink">Meditate</tspan>
      <tspan class="way--green">Write in a journal</tspan>
      <tspan class="way--purple">Go for a walk</tspan>
      <tspan class="way--green">Plant a tree</tspan>
      <tspan class="way--blue">Swing on a swing</tspan>
      <tspan class="way--green">Forgive someone</tspan>
      <tspan class="way--pink">Write a poem</tspan>
      <tspan class="way--green">Hug someone</tspan>
      <tspan class="way--pink">Fake a smile</tspan>
      <tspan class="way--purple">Gaze at the stars</tspan>
      <tspan class="way--green">Play a game</tspan>
      <tspan class="way--blue">Stand up and stretch</tspan>
      <tspan class="way--orange">Paint a picture</tspan>
      <tspan class="way--green">Read a book</tspan>
      <tspan class="way--purple">Look at a work of art</tspan>
      <tspan class="way--blue">Bake some cookies</tspan>
      <tspan class="way--orange">Go for a bike ride</tspan>
      <tspan class="way--pink">Review your achievements</tspan>
      <tspan class="way--green">Relive happy memories</tspan>
      <tspan class="way--blue">Get a haircut</tspan>
      <tspan class="way--green">Pat a dog</tspan>
      <tspan class="way--purple">Volunteer your time</tspan>
      <tspan class="way--blue">Perform an act of kindness</tspan>
      <tspan class="way--pink">Give yourself a time-out</tspan>
      <tspan class="way--purple">Make yourself a cup of tea</tspan>
      <tspan class="way--orange">Listen to a guided relaxation mp3</tspan>
      <tspan class="way--blue">Watch a funny movie</tspan>
      <tspan class="way--orange">Disconnect from technology</tspan>
      <tspan class="way--green">Colour in</tspan>
      <tspan class="way--green">Play in the park</tspan>
      <tspan class="way--pink">Take a class at the gym</tspan>
      <tspan class="way--blue">Get a massage</tspan>
      <tspan class="way--purple">De-clutter a drawer</tspan>
      <tspan class="way--blue">Take a long drive</tspan>
      <tspan class="way--green">Borrow a book from the library</tspan>
      <tspan class="way--blue">Go on a picnic</tspan>
      <tspan class="way--purple">Visit a farmers market</tspan>
      <tspan class="way--pink">Vent</tspan>
      <tspan class="way--blue">Live for today</tspan>
      <tspan class="way--blue">Ask for help</tspan>
      <tspan class="way--purple">Create some routines</tspan>
      <tspan class="way--pink">Scale down your to do list</tspan>
      <tspan class="way--orange">Accept what you can't change</tspan>
      <tspan class="way--green">Compliment yourself often</tspan>
      <tspan class="way--pink">Outsource if you can</tspan>
      <tspan class="way--blue">Write positive self-statements</tspan>
      <tspan class="way--purple">Try Progressive Muscle Relaxation</tspan>
    </textPath>
  </text>

  <text class="poster-title" text-anchor="middle">
    <tspan x="622" y="484">60 Ways to</tspan>
    <tspan x="622" y="518">de-stress</tspan>
  </text>

  <g class="brand">
    <text class="brand-name" x="925" y="853">Willowbrook Calm</text>
    <text class="brand-strapline" x="925" y="873">counselling &amp; coaching for mums</text>
    <circle class="brand-dot" cx="1120" cy="846" r="7"/>
  </g>
</svg>
</body>
</html>
```